Hi
Thank you for considering my job.

I need a layout design for a website. The design should preferably suit GainsLayout Blogcraft layout. Please design according to the attached LAYOUT.GIF

I already have a logo which I like but could be pushed to change if you have an exceptional design. Otherwise I would like to try to incorporate the jigsaw pieces in the design somehow.

Our company is based in Australia and called Parting Toolbox. We have developed a "Sever Pack" to assist both men and women going through divorce to prepare themselves adequately before the seek legal or financial advice to ensure they pay professionals for "advice" and not instructions on basic administration.

I hope the successful candidate will also be able to design a logo and squeeze page and all of the marketing images I will need to accompany The Sever Pack in a few weeks time, though it is not part of this job.

I have attached a very rough guide as to the types of elements and how I would like it to feel. I am not set on any of the fonts or general presentation at all. I feel comfortable with the colour scheme but again, open to ideas. Although the logo has the dark teal green background, I am not sure this works on the web page - open to ideas.

Some must haves:
a video on the front page
an opt in/members' login
link to Orinoco books sales (affiliate widget)
Disclaimer must be visible on first SCREEN

The website must portray a professional, trustworthy and up to date type image - similar to a law firm, accounting firm, bank or university. It must be clean and crisp, inviting and non-gender biased.

Please message me if you have any questions at all.

Thanks again.
Marguerite
Perth, Australia

Target Market(s)

Australian MEN AND WOMEN - 30 - 60 years middle to upper income earners

Industry/Entity Type

Accounting

Requirements
Must have
• Some must haves:
a video on the front page
an opt in/members' login

The website must portray a professional, trustworthy and up to date type image - similar to a law firm, accounting firm BUT SLIGHTLY MORE PEOPLE ORIENTED

```html
<!DOCTYPE html>
<html lang="en">
<head>
<meta charset="utf-8">
<title>Parting Toolbox</title>
<link href="https://fonts.googleapis.com/css2?family=Open+Sans:ital,wght@0,400;0,600;0,700;1,400;1,600;1,700;1,800&display=swap" rel="stylesheet">
<style>
:root{
  --teal:#0b4a55;
  --teal-dark:#062f36;
  --lime:#c9e63c;
  --lime-deep:#a9c82a;
  --cyan:#3ccbe2;
  --orange:#f43f0c;
  --accent:#f05a28;
  --page:#eeeeee;
  --grey-text:#666666;
  --ink:#1e2a2c;
  --white:#ffffff;
}
*{box-sizing:border-box;margin:0;padding:0}
html,body{width:1200px;height:1163px;overflow:hidden}
body{background:var(--page);font-family:"Open Sans",sans-serif;color:var(--ink);position:relative}
.abs{position:absolute}

/* header */
.site-header{position:absolute;left:0;top:0;width:1200px;height:100px;background:var(--teal)}
.brand{position:absolute;left:148px;top:38px;display:flex;align-items:center;gap:10px}
.brand-mark{display:block;width:16px;height:16px;background:var(--lime)}
.brand-name{font-size:22px;font-weight:600;color:var(--white)}
.account{position:absolute;left:762px;top:12px;display:flex;align-items:center;gap:12px;color:var(--white);font-size:13px}
.account span{display:flex;align-items:center;gap:7px}
.account .sep{width:1px;height:18px;background:#3d7c86}
.search{position:absolute;left:762px;top:55px;width:299px;height:24px;background:var(--white);border:1px solid #9bb;display:flex;align-items:center;padding:0 5px;font-size:11px;font-style:italic;color:#555}
.search svg{position:absolute;right:5px;top:3px}

.main-nav,.foot-nav{position:absolute;left:0;width:1200px;height:30px}
.main-nav{top:100px;background:var(--teal-dark)}
.foot-nav{top:1055px;background:#e2e2e2}
.main-nav a,.foot-nav a{position:absolute;font-size:12px;text-decoration:none;text-transform:uppercase;top:8px}
.main-nav a{color:var(--white)}
.foot-nav a{color:#666}
.main-nav .current::after{content:"";position:absolute;left:-13px;right:-13px;top:22px;height:3px;background:var(--accent)}

/* feature boxes */
.panel{position:absolute;border:3px solid var(--white);box-shadow:0 2px 3px rgba(0,0,0,.12)}
.kit{left:138px;top:157px;width:299px;height:273px;background:var(--lime)}
.kit h2{font-size:19px;font-style:italic;font-weight:800;text-align:center;padding-top:8px;height:44px;border-bottom:1px solid #a8c52b;box-shadow:0 1px 0 #e5f79a;color:#111}
.kit .intro{position:absolute;left:12px;top:60px;width:280px;font-size:12px;line-height:19px}
.kit .item{position:absolute;display:flex;align-items:center;gap:8px;font-size:12px;font-weight:600;font-style:italic;color:var(--teal);line-height:19px}
.kit .foot{position:absolute;left:42px;top:228px;width:250px;font-size:10.5px;font-style:italic;line-height:18px}

.tool{left:138px;top:445px;width:299px;height:78px;background:var(--orange)}
.tool p{position:absolute;left:20px;top:18px;font-size:18px;font-weight:800;font-style:italic;line-height:19px;color:var(--white);text-shadow:1px 1px 0 #5a1500}

.video{left:451px;top:157px;width:298px;height:366px;background:var(--cyan)}
.video h2{font-size:17px;font-style:italic;font-weight:800;text-align:center;line-height:19px;padding-top:3px;height:44px;border-bottom:1px solid #1aa9c0;color:#111}
.video .intro{position:absolute;left:10px;top:57px;width:280px;font-size:11.6px;line-height:18px;color:#123}
.player{position:absolute;left:7px;top:171px;width:280px;height:186px;background:#222}
.footage{position:absolute;left:0;top:0;width:280px;height:156px;background:linear-gradient(110deg,#d6cdc6 0%,#9a7d6e 40%,#5a3b2e 60%,#8fae70 100%)}
.controls{position:absolute;left:0;top:156px;width:280px;height:30px;background:linear-gradient(#333,#111)}

.query{left:764px;top:157px;width:297px;height:164px;background:linear-gradient(#b7d52a,var(--lime) 40%);border-bottom:none}
.query .q{position:absolute;right:8px;top:10px;font-size:16px;font-weight:700;font-style:italic;color:var(--teal)}
.query .step{position:absolute;left:6px;display:flex;align-items:center;gap:10px;font-size:16px;font-weight:700;font-style:italic;color:var(--teal)}
.buy{left:764px;top:318px;width:297px;height:205px;background:var(--teal);border-top:2px dashed var(--lime-deep)}
.book{position:absolute;left:14px;top:18px;width:96px;height:128px;background:linear-gradient(160deg,#2e7fa8,#4ba44a 55%,#7bbf3a);transform:skewY(-4deg)}
.buy h3{position:absolute;left:145px;top:12px;font-size:26px;font-weight:800;font-style:italic;color:var(--white)}
.price{position:absolute;left:165px;top:52px;width:82px;height:82px;border-radius:50%;background:radial-gradient(circle at 40% 30%,#fff27a,#ffd000 55%,#e0a600);border:2px solid #fff6a0;text-align:center;font-weight:800;font-style:italic;color:#111}
.price b{display:block;font-size:22px;line-height:22px;margin-top:10px}
.price span{font-size:25px;line-height:28px}
.buy .copy{position:absolute;left:6px;top:150px;font-size:12.5px;font-style:italic;line-height:16px;color:var(--white)}

.nub{position:absolute;background:var(--white);border-radius:50%}

/* articles */
.section-title{position:absolute;font-size:17px;font-weight:600;color:#555}
.arrows{position:absolute;display:flex;gap:14px}
.article{position:absolute;top:596px;width:310px;white-space:nowrap}
.article h4{font-size:13.5px;font-weight:700;font-style:italic;line-height:15px;color:var(--teal)}
.article p{font-size:12.8px;line-height:18.4px;color:var(--grey-text);margin-top:6px}
.article .views{font-size:12.8px;font-weight:600;color:var(--accent);margin-top:8px}
.rule{position:absolute;left:138px;width:922px;height:1px;background:#d4d4d4}

/* community */
.perk{position:absolute;top:817px;width:193px;height:65px;border:2px solid var(--white);display:flex;align-items:center;gap:10px;padding-left:12px;font-size:12.5px;font-weight:600;line-height:15px;white-space:nowrap}
.perk.lime{left:138px;background:var(--lime);color:#111}
.perk.orange{left:346px;background:var(--orange);color:var(--white)}
.perk.cyan{left:553px;background:var(--cyan);color:#123;font-size:12.2px;gap:8px;padding-left:10px}
.quote{position:absolute;left:763px;top:813px;width:297px;height:72px;background:#dcdcdc;padding:7px 12px;font-size:12.5px;line-height:18.4px;color:var(--grey-text);white-space:nowrap}
.quote::after{content:"";position:absolute;left:126px;top:72px;border-left:28px solid transparent;border-top:18px solid #dcdcdc}
.quote-by{position:absolute;left:933px;top:893px;font-size:13.5px;font-weight:600;color:var(--accent)}

.disclaimer h3{position:absolute;left:137px;top:960px;font-size:17px;font-weight:400;color:#444}
.disclaimer p{position:absolute;left:140px;top:990px;font-family:Arial,sans-serif;font-size:12.2px;font-weight:700;color:#111}

.social{position:absolute;left:533px;top:1099px;display:flex;gap:7px}
.social i{display:block;width:29px;height:29px;border-radius:50%;background:#c6c6c6}
.copyright{position:absolute;left:0;width:1200px;top:1140px;text-align:center;font-size:11px;color:#888}
</style>
</head>
<body>

<header class="site-header">
  <div class="brand"><i class="brand-mark"></i><span class="brand-name">Parting Toolbox</span></div>
  <div class="account">
    <span><svg width="18" height="18" viewBox="0 0 18 18"><circle cx="9" cy="5" r="4" fill="#fff"/><path d="M1 17c0-5 4-7 8-7s8 2 8 7z" fill="#fff"/></svg>Login</span>
    <i class="sep"></i>
    <span><svg width="20" height="20" viewBox="0 0 20 20"><rect x="1.5" y="4.5" width="13" height="13" fill="none" stroke="#fff" stroke-width="2"/><path d="M7 12l1-3 8-8 2 2-8 8z" fill="#fff"/></svg>Register</span>
  </div>
  <div class="search">Search<svg width="17" height="17" viewBox="0 0 17 17"><circle cx="7" cy="7" r="5" fill="none" stroke="#333" stroke-width="2.2"/><path d="M11 11l5 5" stroke="#333" stroke-width="3"/></svg></div>
</header>

<nav class="main-nav">
  <a class="current" style="left:151px">Home</a><a style="left:219px">Considering Divorce?</a><a style="left:386px">Legal Process</a><a style="left:507px">Parenting</a><a style="left:604px">Property &amp; Finance</a><a style="left:757px">Community</a><a style="left:859px">Tools</a><a style="left:928px">FAQs</a><a style="left:989px">About Us</a>
</nav>

<section class="panel kit">
  <h2>Try our Sever Pack</h2>
  <p class="intro">Lorem ipsum dolor sit amet consectetur adipisicing elitsed do eiusmod tempor incididun.</p>
  <div class="item" style="left:4px;top:117px"><svg width="32" height="44" viewBox="0 0 32 44"><circle cx="16" cy="9" r="7" fill="none" stroke="#fff" stroke-width="3"/><path d="M3 42V28c0-7 6-10 13-10s13 3 13 10v14z" fill="none" stroke="#fff" stroke-width="3"/><path d="M16 20v14" stroke="#fff" stroke-width="3"/></svg><span>Administration<br>Support</span></div>
  <div class="item" style="left:144px;top:122px"><svg width="48" height="44" viewBox="0 0 48 44"><path d="M6 2h28v30l-10 10H6z" fill="#fff"/><path d="M24 42V32h10" fill="#ddd"/><path d="M10 30L28 12l4 4-18 18-6 2z" fill="var(--lime)"/></svg><span>Documentation<br>Prepration</span></div>
  <div class="item" style="left:6px;top:190px"><svg width="30" height="44" viewBox="0 0 30 44"><text x="15" y="38" text-anchor="middle" font-family="Open Sans,sans-serif" font-size="44" font-weight="700" fill="#fff">$</text></svg><span>Finances<br>Support</span></div>
  <div class="item" style="left:148px;top:190px"><svg width="46" height="44" viewBox="0 0 46 44"><circle cx="23" cy="11" r="10" fill="#fff"/><path d="M2 44c0-14 9-20 21-20s21 6 21 20z" fill="#fff"/><path d="M21 25h4l2 14-4 4-4-4z" fill="var(--lime)"/></svg><span>Professional<br>Advisor</span></div>
  <p class="foot">Lorem ipsum dolor sit amet consectetur  elitsed do eiusmod.</p>
  <i class="nub" style="left:8px;top:252px;width:14px;height:14px"></i>
</section>

<section class="panel tool">
  <p>Try our Free<br>Parting Tool</p>
  <svg class="abs" style="left:198px;top:10px" width="56" height="54" viewBox="0 0 56 54"><path d="M6 48L40 14" stroke="#fff" stroke-width="7" stroke-linecap="round"/><path d="M32 6l18 18-6 6-18-18z" fill="#fff"/><path d="M50 48L20 18" stroke="#fff" stroke-width="6" stroke-linecap="round"/><circle cx="14" cy="12" r="9" fill="none" stroke="#fff" stroke-width="5"/></svg>
  <i class="nub" style="left:280px;top:2px;width:14px;height:14px"></i>
</section>

<section class="panel video">
  <h2>Watch the video now to<br>discover what it's all about...</h2>
  <p class="intro">Lorem ipsum dolor sit amet consectetur adipisicing elitsed do eiusmod tempor incididunt ut labore et dolore magna aliqua. Ut enim ad minim veniam, quis nostrud exercitation ullamco laboris nisi ut aliquip ex ea commodo consequat.</p>
  <div class="player">
    <div class="footage" role="img" aria-label="Video still of a presenter seated outdoors"></div>
    <svg class="abs" style="left:110px;top:56px" width="56" height="56" viewBox="0 0 56 56"><circle cx="28" cy="28" r="27" fill="rgba(0,0,0,.55)"/><path d="M21 15l20 13-20 13z" fill="#ddd"/></svg>
    <div class="controls">
      <svg width="280" height="30" viewBox="0 0 280 30"><rect x="0" y="0" width="280" height="3" fill="#555"/><rect x="0" y="0" width="130" height="3" fill="#d00"/><circle cx="130" cy="2" r="5" fill="#eee"/><rect x="21" y="13" width="3" height="10" fill="#ddd"/><rect x="27" y="13" width="3" height="10" fill="#ddd"/><path d="M56 15h4l5-4v14l-5-4h-4z" fill="#ddd"/><text x="85" y="22" font-family="Open Sans,sans-serif" font-size="10" fill="#fff" font-weight="700">0:30 <tspan fill="#bbb" font-weight="400">/ 2:10</tspan></text><rect x="158" y="13" width="14" height="9" rx="2" fill="none" stroke="#ddd" stroke-width="1.5"/><circle cx="190" cy="18" r="5" fill="none" stroke="#ddd" stroke-width="3"/><rect x="208" y="14" width="14" height="8" fill="none" stroke="#ddd" stroke-width="1.5"/><rect x="232" y="12" width="18" height="11" fill="none" stroke="#ddd" stroke-width="1.5"/><path d="M260 12h4M260 12v4M274 12h-4M274 12v4M260 24h4M260 24v-4M274 24h-4M274 24v-4" stroke="#ddd" stroke-width="1.5"/></svg>
    </div>
  </div>
  <i class="nub" style="left:270px;top:-1px;width:16px;height:16px"></i>
</section>

<section class="panel query">
  <span class="q">Query?</span>
  <div class="step" style="top:16px"><svg width="36" height="40" viewBox="0 0 36 40"><path d="M18 2l15 6v12c0 10-7 16-15 19C10 36 3 30 3 20V8z" fill="var(--teal)"/><text x="18" y="28" text-anchor="middle" font-family="Open Sans,sans-serif" font-size="20" font-weight="700" fill="var(--lime)">?</text></svg>ask a question</div>
  <div class="step" style="top:64px"><svg width="38" height="38" viewBox="0 0 38 38"><circle cx="16" cy="10" r="8" fill="var(--teal)"/><path d="M1 37c0-12 7-17 15-17 5 0 9 2 12 6l-3 11z" fill="var(--teal)"/><path d="M31 24v12M25 30h12" stroke="var(--teal)" stroke-width="4"/></svg>expert answer</div>
  <div class="step" style="top:108px"><svg width="36" height="36" viewBox="0 0 36 36"><circle cx="18" cy="18" r="16" fill="none" stroke="var(--teal)" stroke-width="3"/><circle cx="12" cy="14" r="2.5" fill="var(--teal)"/><circle cx="24" cy="14" r="2.5" fill="var(--teal)"/><path d="M10 21c3 6 13 6 16 0" fill="none" stroke="var(--teal)" stroke-width="3"/></svg>accept if satisfied</div>
</section>

<section class="panel buy">
  <div class="book" role="img" aria-label="Cover of a family relationships guide book"></div>
  <h3>Buy Now</h3>
  <div class="price"><b>$</b><span>12.99</span></div>
  <p class="copy">Download immediately.<br>This simple guide provides a<br>wealth of essential information.</p>
  <svg class="abs" style="left:220px;top:160px" width="22" height="24" viewBox="0 0 22 24"><path d="M2 2l18 10L2 22z" fill="var(--lime)"/></svg>
  <i class="nub" style="left:266px;top:154px;width:26px;height:26px"></i>
</section>

<h2 class="section-title" style="left:138px;top:557px">Most Popular Articles</h2>
<div class="arrows" style="left:1000px;top:555px">
  <svg width="22" height="24" viewBox="0 0 22 24"><path d="M18 2L6 12l12 10" fill="none" stroke="#bbb" stroke-width="4"/></svg>
  <svg width="22" height="24" viewBox="0 0 22 24"><path d="M4 2l12 10L4 22" fill="none" stroke="#bbb" stroke-width="4"/></svg>
</div>

<article class="article" style="left:139px"><h4>Lorem ipsum dolor sit amet elitsed incididunt<br>eiusmod Ut enim minim veniam.</h4><p>Lorem ipsum dolor sit amet adipisicing elitsed<br>do eiusmod tempor incididunt ut labore et<br>dolore magna aliqua. Ut enim minim veniam,<br>aliquip ex ea commodo consequat.</p><p class="views">[378 views in Aug]</p></article>
<article class="article" style="left:457px"><h4>Lorem ipsum dolor sit amet elited incidunt<br>eiusmod Ut enim minim veniam.</h4><p>Lorem ipsum dolor sit amet adipisicing elitsed<br>do eiusmod tempor incididunt ut labore et<br>dolore magna aliqua. Ut enim minim veniam,<br>aliquip ex ea commodo consequat.</p><p class="views">[378 views in Aug]</p></article>
<article class="article" style="left:768px"><h4>Lorem ipsum dolor sit amet elited incidunt<br>eiusmod Ut enim minim veniam.</h4><p>Lorem ipsum dolor sit amet adipisicing elitsed<br>do eiusmod tempor incididunt ut labore et<br>dolore magna aliqua. Ut enim minim veniam,<br>aliquip ex ea commodo consequat.</p><p class="views">[378 views in Aug]</p></article>

<div class="rule" style="top:760px;background:linear-gradient(90deg,transparent,#ccc 10%,#ccc 90%,transparent);height:3px"></div>

<h2 class="section-title" style="left:136px;top:780px">Join our community</h2>
<div class="perk lime"><svg width="38" height="24" viewBox="0 0 38 24"><circle cx="11" cy="7" r="5" fill="#333"/><circle cx="27" cy="7" r="5" fill="#333"/><circle cx="19" cy="9" r="6" fill="#222"/><path d="M2 22c0-7 4-10 9-10s9 3 9 10zM18 22c0-7 4-10 9-10s9 3 9 10z" fill="#333"/><path d="M9 24c0-8 5-11 10-11s10 3 10 11z" fill="#222"/></svg>Free membership</div>
<div class="perk orange"><svg width="24" height="32" viewBox="0 0 24 32"><rect x="1" y="1" width="22" height="30" rx="3" fill="#3a1206"/><rect x="4" y="4" width="16" height="7" fill="var(--orange)"/><g fill="var(--orange)"><rect x="4" y="14" width="4" height="3"/><rect x="10" y="14" width="4" height="3"/><rect x="16" y="14" width="4" height="3"/><rect x="4" y="20" width="4" height="3"/><rect x="10" y="20" width="4" height="3"/><rect x="16" y="20" width="4" height="3"/><rect x="4" y="26" width="4" height="3"/><rect x="10" y="26" width="4" height="3"/><rect x="16" y="26" width="4" height="3"/></g></svg><span>Instant access to<br>calculators and<br>tools</span></div>
<div class="perk cyan"><svg width="26" height="26" viewBox="0 0 28 28"><rect x="2" y="6" width="20" height="20" fill="none" stroke="#123" stroke-width="2.5"/><path d="M10 18l1-4 12-12 3 3-12 12z" fill="#123"/></svg><span>Anonymous and free<br>participation in support<br>and advice forums</span></div>
<i class="nub" style="left:317px;top:821px;width:10px;height:10px"></i>
<i class="nub" style="left:522px;top:862px;width:14px;height:14px"></i>
<i class="nub" style="left:556px;top:819px;width:10px;height:10px"></i>

<h2 class="section-title" style="left:767px;top:780px">Client Testimonials</h2>
<div class="arrows" style="left:1000px;top:779px">
  <svg width="22" height="24" viewBox="0 0 22 24"><path d="M18 2L6 12l12 10" fill="none" stroke="#bbb" stroke-width="4"/></svg>
  <svg width="22" height="24" viewBox="0 0 22 24"><path d="M4 2l12 10L4 22" fill="none" stroke="#bbb" stroke-width="4"/></svg>
</div>
<blockquote class="quote">Lorem ipsum dolor sit amet adipisicing elitsed<br>do eiusmod tempor amet incididunt ut labore<br>et dolore magna aliqua. Ut enim minim</blockquote>
<p class="quote-by">Lorem Ipsum text</p>

<div class="rule" style="top:938px"></div>
<section class="disclaimer">
  <h3>Disclaimer</h3>
  <p>Lorem ipsum dolor sit amet consectetur adipisicing elitsed do eiusmod tempor incididunt ut labore et dolore aliqua. Ut enim ad minim veniam, quis nostrud</p>
</section>

<nav class="foot-nav">
  <a style="left:151px">Home</a><a style="left:219px">Considering Divorce?</a><a style="left:386px">Legal Process</a><a style="left:507px">Parenting</a><a style="left:604px">Property &amp; Finance</a><a style="left:757px">Community</a><a style="left:859px">Tools</a><a style="left:928px">FAQs</a><a style="left:989px">About Us</a>
</nav>

<div class="social"><i></i><i></i><i></i><i></i></div>
<p class="copyright">© 2013 - PartingToolbox.&nbsp;&nbsp; | &nbsp;&nbsp;Terms &amp; Privacy</p>

</body>
</html>
```